Homepage Erstellung für neues Online Unternehmen Flinkemeister-Portal.de
Zielgruppe
Ziel von www.Flinkemeister-Portal.de ist der Vergleich / Suche des günstigsten Handwerkers in allen Gewerken.
Aktuell befindet sich unter der Adresse nur eine Übersicht wie das Konzept des Unternehmens im Groben aussieht. Ein Logo wird ebenfalls gesucht.
Aufgabenstellung
Es soll eine Webseite erstellt werden, die klar und strukturiert ist, damit sich potentielle Kunden schnell zurecht finden. Dem Kunden sollte einen professionellen Eindruck (seriös, kompetent, leistungsstark und einfach) erhalten.
Das Design sollte zum Handwerk passen und modern in der Zeit sein. Wichtig ist, dass sowohl die Startseite als auch ein Kontaktformular erstellt wird. Der Aufbau kann gerne der gleiche sein im Design, analog die Aufgabe / Beschreibung des Unternehmens.
Da es sich um ein frisch gegründet und im Aufbau befindliches Unternehmen handelt sind wir für alle Ideen, Vorschläge offen.
Bei Abweichung der Seitenanzahl, Logo erstellung etc sollte selbstverständlich sein, dass der Preis noch abweichend von dem angezeigten Preis ist. Dazu bitte eine Budget Angabe mit abgeben. Vielen Dank

```html
<!DOCTYPE html>
<html lang="de">
<head>
<meta charset="utf-8">
<title>Flinkemeister-Portal.de – Startseite</title>
<link href="https://fonts.googleapis.com/css2?family=Russo+One&family=Arimo:wght@400;700&display=swap" rel="stylesheet">
<style>
  :root {
    --page-bg: #ffffff;
    --header-bg: #c5876a;
    --header-bg-dark: #b9785a;
    --nav-bg: #e9ab8b;
    --nav-active: #c68868;
    --nav-divider: #cf8f70;
    --nav-text: #8a4326;
    --brand-text: #ffffff;
    --tagline: #8a4a2e;
    --cream: #fbf0e3;
    --heading-dark: #3b1d12;
    --heading-light: #f2c07e;
    --body-text: #7a3a1c;
    --footer-bg: #3a1a10;
    --footer-copy: #f1b77c;
    --social-dot: #e9a27c;
  }
  * { box-sizing: border-box; margin: 0; padding: 0; }
  html, body { width: 1200px; height: 806px; overflow: hidden; background: var(--page-bg); }
  body { font-family: "Arimo", Arial, sans-serif; position: relative; }

  .site { position: absolute; left: 136px; top: 0; width: 929px; height: 806px; }

  .site-header {
    position: absolute; left: 0; top: 0; width: 929px; height: 111px;
    background: linear-gradient(135deg, var(--header-bg), var(--header-bg-dark));
  }
  .brand { position: absolute; left: 25px; top: 29px; }
  .brand-name {
    font-family: "Russo One", sans-serif; font-size: 33px; line-height: 1;
    color: var(--brand-text); letter-spacing: 0.6px; white-space: nowrap;
  }
  .brand-tagline {
    margin-top: 4px; font-family: "Arimo", Arial, sans-serif; font-weight: 700;
    font-size: 13px; letter-spacing: 3.4px; color: var(--tagline); white-space: nowrap;
  }
  .social { position: absolute; right: 38px; top: 24px; display: flex; gap: 20px; align-items: center; }
  .social-link { display: flex; align-items: center; gap: 9px; color: #fff; font-size: 12px; text-decoration: none; }
  .social-dot { width: 30px; height: 30px; border-radius: 50%; background: var(--social-dot); box-shadow: 0 1px 2px rgba(0,0,0,.25); }

  .main-nav {
    position: absolute; left: 0; top: 111px; width: 929px; height: 76px;
    display: flex; background: var(--nav-bg);
  }
  .nav-item {
    flex: 1; display: flex; align-items: center; justify-content: center;
    font-family: "Arimo", Arial, sans-serif; font-weight: 700; font-size: 14px;
    color: var(--nav-text); text-decoration: none; border-left: 1px solid var(--nav-divider);
  }
  .nav-item:first-child { border-left: none; }
  .nav-item.is-active { background: var(--nav-active); color: #fff; }

  .content { position: absolute; left: 0; top: 187px; width: 929px; height: 580px; }
  .side-left { position: absolute; left: 0; top: 0; width: 318px; height: 580px; background: var(--cream); }
  .photo-roof {
    position: absolute; left: 0; top: 0; width: 318px; height: 307px;
    background: linear-gradient(160deg, #c86f4e 0%, #e7a384 35%, #f3c6ad 70%, var(--cream) 100%);
  }
  .side-right { position: absolute; left: 798px; top: 0; width: 131px; height: 580px; background: var(--cream); }
  .photo-plumbing {
    position: absolute; left: 0; top: 0; width: 131px; height: 404px;
    background: linear-gradient(180deg, #e8e6e2 0%, #c9b29a 40%, #8f8a86 68%, var(--cream) 100%);
  }

  .welcome { position: absolute; left: 318px; top: 0; width: 480px; height: 580px; background: #fff; padding: 30px 30px 0 33px; }
  .welcome-title { font-family: "Russo One", sans-serif; font-size: 33px; font-weight: 400; letter-spacing: 0.6px; color: var(--heading-dark); line-height: 1; white-space: nowrap; }
  .welcome-title .accent { color: var(--heading-light); }
  .welcome-lead { margin-top: 20px; max-width: 370px; font-weight: 700; font-size: 13.5px; line-height: 19.5px; color: var(--body-text); }
  .welcome-text { margin-top: 19px; font-size: 11.6px; line-height: 19.4px; color: var(--body-text); }

  .site-footer {
    position: absolute; left: 0; top: 767px; width: 929px; height: 39px;
    background: var(--footer-bg); display: flex; align-items: center; justify-content: space-between;
    padding: 0 14px 0 12px;
  }
  .to-top { display: flex; align-items: center; gap: 6px; color: #fff; font-size: 11.5px; text-decoration: none; }
  .copyright { color: var(--footer-copy); font-size: 11.5px; }
</style>
</head>
<body>
<div class="site">
  <header class="site-header">
    <div class="brand">
      <div class="brand-name">FLINKEMEISTER-PORTAL.de</div>
      <div class="brand-tagline">IHRE ONLINESUCHE DES GÜNSTIGSTEN HANDWERKERS</div>
    </div>
    <div class="social">
      <a class="social-link" href="#">Treffpunkt <span class="social-dot"></span></a>
      <a class="social-link" href="#">Kurznotiz <span class="social-dot"></span></a>
    </div>
  </header>

  <nav class="main-nav">
    <a class="nav-item is-active" href="#">STARTSEITE</a>
    <a class="nav-item" href="#">PREIS &amp; LEISTUNG</a>
    <a class="nav-item" href="#">SERVICE</a>
    <a class="nav-item" href="#">KONTAKT</a>
    <a class="nav-item" href="#">IMPRESSUM</a>
  </nav>

  <main class="content">
    <aside class="side-left">
      <div class="photo-roof" role="img" aria-label="Foto: Dachdecker verlegt rote Dachziegel"></div>
    </aside>

    <section class="welcome">
      <h1 class="welcome-title">HERZLICH <span class="accent">WILLKOMMEN</span></h1>
      <p class="welcome-lead">Unsere Aufgabe ist es für Sie vorhandene Angebote zu günstigeren konditionen zu beschaffen aber auch ohne Angebot suchen wir für Sie den billigsten Handwerker.</p>
      <p class="welcome-text">Durch hochwertige Arbeit, flexiblen Service und hohen persönlichen Einsatz können wir unseren Kundenkreis stetig erweitern. Bei uns können Sie zuverlässige und professionelle Arbeit auf hohem Niveau erwarten! Überzeugen Sie sich am Besten selbst davon.</p>
      <p class="welcome-text">Wir freuen uns auf Ihre Anfrage - nehmen sie kontakt zu uns auf.</p>
    </section>

    <aside class="side-right">
      <div class="photo-plumbing" role="img" aria-label="Foto: Installateur repariert Siphon unter einem Waschbecken"></div>
    </aside>
  </main>

  <footer class="site-footer">
    <a class="to-top" href="#">
      <svg width="30" height="30" viewBox="0 0 30 30" aria-hidden="true">
        <circle cx="15" cy="15" r="14" fill="#1f0d07"/>
        <path d="M10.5 17.5 L15 12 L19.5 17.5 Z" fill="#fff"/>
      </svg>
      Nach oben
    </a>
    <span class="copyright">Copyright 2013 Flinkemeister-Portal.de - Alle Rechte vorbehalten</span>
  </footer>
</div>
</body>
</html>
```